QuintaraHC Postcard Design

We need a postcard design for our home health care company in Albuquerque, NM. The services we offer are home healthcare services. I included a digital brochure for reference.

Target Market(s)

elderly people and/or people looking for home health services

Industry/Entity Type

Home Health Care

Requirements
Must have
• Must have our moto "Bringing Quality Care Home". Must have our contact information including website. Must have our logo.
Nice to have
• picture of caregiver and client or picture of elderly couple

```html
<!DOCTYPE html>
<html lang="en">
<head>
<meta charset="utf-8">
<title>QuintaraHC Postcard</title>
<link href="https://fonts.googleapis.com/css2?family=Cinzel:wght@400&family=Tinos&family=Arimo&display=swap" rel="stylesheet">
<style>
  :root {
    --bg: #ecebe8;
    --brand-blue: #1557ad;
    --brand-light: #7e91d6;
    --paper: #ffffff;
    --rule: #8a8a8a;
    --ink: #333333;
    --photo-warm-a: #e9dccd;
    --photo-warm-b: #b79a8a;
    --photo-cool-a: #dfe3ea;
    --photo-cool-b: #9ea6b4;
  }
  * { margin: 0; padding: 0; box-sizing: border-box; }
  html, body { width: 1200px; height: 1021px; overflow: hidden; }
  body {
    background: var(--bg);
    position: relative;
  }
  .postcard {
    position: absolute;
    width: 560px;
    height: 440px;
    background: var(--paper);
    overflow: hidden;
    box-shadow: 0 2px 10px rgba(0,0,0,0.18);
  }
  .postcard--front { left: 30px; top: 290px; }
  .postcard--back { left: 610px; top: 290px; display: flex; }

  /* front */
  .front-photo {
    position: absolute; inset: 0;
    background: linear-gradient(135deg, var(--photo-warm-a) 0%, #d8c8bc 45%, var(--photo-warm-b) 100%);
  }
  .front-panel { position: absolute; inset: 0; }
  .brand-name {
    position: absolute;
    left: 38px; top: 36px;
    font-family: "Cinzel", serif;
    font-weight: 400;
    font-size: 26px;
    line-height: 1.1;
    color: var(--brand-blue);
    letter-spacing: 1px;
  }
  .tagline {
    position: absolute;
    right: 36px; top: 236px;
    font-family: "Cinzel", serif;
    font-size: 25px;
    line-height: 1.22;
    color: var(--paper);
    text-align: right;
    letter-spacing: 1px;
  }

  /* back */
  .back-left {
    width: 50%;
    height: 100%;
    display: flex;
    flex-direction: column;
  }
  .back-photo {
    height: 56%;
    background: linear-gradient(120deg, var(--photo-cool-b) 0%, var(--photo-cool-a) 50%, #c9b8aa 100%);
  }
  .back-band { height: 10px; background: var(--brand-light); }
  .back-contact {
    flex: 1;
    background: var(--brand-blue);
    color: var(--paper);
    font-family: "Tinos", serif;
    font-size: 13px;
    line-height: 1.45;
    text-align: center;
    display: flex;
    flex-direction: column;
    justify-content: flex-end;
    padding-bottom: 22px;
  }
  .back-right {
    width: 50%;
    height: 100%;
    position: relative;
  }
  .stamp-box {
    position: absolute;
    right: 24px; top: 22px;
    width: 74px; height: 74px;
    border: 1px solid var(--rule);
    font-family: "Arimo", sans-serif;
    font-size: 9px;
    color: var(--ink);
    display: flex; align-items: center; justify-content: center;
  }
  .address-lines {
    position: absolute;
    left: 16px; right: 24px; top: 158px;
    list-style: none;
  }
  .address-lines li {
    height: 44px;
    border-bottom: 1px solid var(--rule);
  }
  .address-lines li:first-child { height: 0; }
</style>
</head>
<body>
  <section class="postcard postcard--front">
    <div class="front-photo" role="img" aria-label="Photo of a smiling caregiver with an elderly woman at home"></div>
    <svg class="front-panel" viewBox="0 0 560 440" width="560" height="440" aria-hidden="true">
      <path d="M300 0 C420 110 400 320 230 440 L560 440 L560 0 Z" fill="#ffffff"/>
      <path d="M316 0 C436 110 416 320 250 440 L560 440 L560 0 Z" fill="var(--brand-light)"/>
      <path d="M336 0 C452 110 432 320 272 440 L560 440 L560 0 Z" fill="var(--brand-blue)"/>
    </svg>
    <div class="brand-name">Quintara<br>Home Care</div>
    <p class="tagline">Bringing<br>Quality<br>Care Home</p>
  </section>

  <section class="postcard postcard--back">
    <div class="back-left">
      <div class="back-photo" role="img" aria-label="Photo of a smiling elderly couple"></div>
      <div class="back-band"></div>
      <address class="back-contact" style="font-style:normal">
        <span>2740 Mesa Vista Loop NE</span>
        <span>Albuquerque, NM 87110</span>
        <span>505-555-0186</span>
        <span>www.QuintaraHomeCare.com</span>
      </address>
    </div>
    <div class="back-right">
      <div class="stamp-box">STAMP</div>
      <ul class="address-lines">
        <li></li><li></li><li></li><li></li><li></li>
      </ul>
    </div>
  </section>
</body>
</html>
```